Professional Business Card for Luxury Hotel & Resort Development Firm. Advisory firm

Project Overview: We are a specialized advisory firm focused on Hotel & Resort Development. Our clients are high-net-worth investors and major hospitality brands.

Design Requirements:

Style: Minimalist, sophisticated, and trustworthy. We want to avoid looking too "corporate" or "dry"—it should feel premium.

Key Elements: Please incorporate our logo [もしロゴがあれば] and emphasize a clean layout with plenty of white space.

Color Palette: We prefer Grey and White or Black and White to evoke a sense of luxury and stability.

Typography: Professional garamond, or sans-serif or elegant serif fonts

Goal: The card should feel substantial and high-end when handed to a client, reflecting our expertise in multi-million dollar developments.
Updates

I am currently on a business trip for field research and have limited access to my desktop. Additionally, I have just provided detailed technical feedback to a designer and am waiting for their refined proposals. To ensure the final logo meets the high standards of my new advisory firm, I would like to extend the deadline by 7 days. Thank you for your support.

Target Market(s)

High-net-worth investors, luxury hospitality brands, and real estate developers.

Contact Information for Business Card

Firm Name: Harbor Crest Partners, My Name: Kenji Morisawa, Title: Founder, Address 5-8-4 Kitanomura Aoba Yokohama Japan 225-0143, email address: kmorisawa@harborcrestpx.example, Tel: +81 90-4183-2750. Front Site (Primary): Japanese translation of the back side, Please use a clean Japanese font (like Mincho) that complements the Garmond on the English side Back side: English. Note for Japanese text: since the frond side is the main fae, please ensure the layout is clean and professional. Please use a high-quality Mincho ( Serif-style) font for Japanese to mach the Garmond used on the English side. Text for Front side (Japanese) Harbor Crest Partners, 役職:代表、森沢健二、225-0143 横浜市青葉区北野村5-8-4. Name of the firm can stay in English.

Font styles to use
Other font styles liked:
• Font Preference: Please use Garamond for all text to maintain a consistent, elegant, and classic professional look.

Requirements
Must have
• Professional and clean layout, high-end feel.
Nice to have
• Minimalist design with subtle luxury accents.

```html
<!DOCTYPE html>
<html lang="ja">
<head>
<meta charset="utf-8">
<title>Harbor Crest Partners — Business Card</title>
<link rel="stylesheet" href="https://fonts.googleapis.com/css2?family=Cormorant+Garamond:ital,wght@0,400;0,500;1,400&family=Shippori+Mincho:wght@400&display=swap">
<style>
  :root {
    --board: #e7e7e7;
    --paper: #f7f7f7;
    --taupe: #bab2a4;
    --white: #ffffff;
  }
  * { margin: 0; padding: 0; box-sizing: border-box; }
  html, body { width: 1200px; height: 1067px; overflow: hidden; }
  body {
    position: relative;
    background: var(--board);
    font-family: "Cormorant Garamond", Garamond, serif;
  }
  .swatch { position: absolute; left: 0; width: 17px; }
  .swatch--taupe { top: 50px; height: 100px; background: var(--taupe); }
  .swatch--paper { top: 150px; height: 100px; background: var(--paper); }

  .brand-mark {
    position: absolute; left: 50px; top: 120px;
    color: var(--taupe);
    font-weight: 500; font-size: 26px; letter-spacing: 0.08em;
    line-height: 1.15; text-transform: uppercase;
  }

  .card {
    position: absolute; left: 333px; width: 667px;
    border-radius: 33px;
  }
  .card--front { top: 100px; height: 403px; background: var(--paper); color: var(--taupe); }
  .card--back  { top: 563px; height: 401px; background: var(--taupe); color: var(--white); }

  .card__identity {
    position: absolute; right: 44px; top: 44px; text-align: right;
  }
  .card__name-ja {
    font-family: "Shippori Mincho", serif;
    font-size: 24px; letter-spacing: 0.12em; line-height: 1.2;
  }
  .card__title-ja {
    font-family: "Shippori Mincho", serif;
    font-size: 15px; letter-spacing: 0.1em; margin-top: 2px;
  }
  .card__name-en {
    font-size: 23px; letter-spacing: 0.03em; line-height: 1.1;
    text-transform: uppercase;
  }
  .card__title-en { font-style: italic; font-size: 20px; line-height: 1; }

  .card__contact {
    position: absolute; right: 44px; bottom: 40px; text-align: right;
    font-style: italic; font-size: 21px; line-height: 28px;
  }
  .card__contact .ja {
    font-family: "Shippori Mincho", serif; font-style: normal; font-size: 17px;
  }

  .card__brand {
    position: absolute; left: 44px; bottom: 42px;
    font-weight: 500; font-size: 22px; letter-spacing: 0.1em;
    line-height: 1.2; text-transform: uppercase;
  }
</style>
</head>
<body>
  <div class="swatch swatch--taupe"></div>
  <div class="swatch swatch--paper"></div>

  <div class="brand-mark">Harbor Crest<br>Partners</div>

  <section class="card card--front" lang="ja">
    <div class="card__identity">
      <p class="card__name-ja">森沢健二</p>
      <p class="card__title-ja">代表</p>
    </div>
    <div class="card__brand" lang="en">Harbor Crest<br>Partners</div>
    <address class="card__contact">
      <p>225-0143</p>
      <p><span class="ja">横浜市青葉区北野村</span>5-8-4</p>
      <p>kmorisawa@harborcrestpx.example</p>
      <p>090-4183-2750</p>
    </address>
  </section>

  <section class="card card--back" lang="en">
    <div class="card__identity">
      <p class="card__name-en">Kenji Morisawa</p>
      <p class="card__title-en">founder</p>
    </div>
    <div class="card__brand">Harbor Crest<br>Partners</div>
    <address class="card__contact">
      <p>5-8-4, Kitanomura Aoba,</p>
      <p>Yokohama, Japan. 225-0143</p>
      <p>kmorisawa@harborcrestpx.example</p>
      <p>+81 90-4183-2750</p>
    </address>
  </section>
</body>
</html>
```